Wine Label front and back- Need to have an eye catching, classy wine label for restaurant placement.

label design for a wine label. eye catching for shelf placement. looking for simple and elegant label. Name of the vineyard will be the label recognition. Need back label to match with coloring and basic regulated info required by gov't (producer, address, and statement) Back label will be addressed after selected front label to match.
Will add $100 extra for the back label to match.

Target Market(s)

40-65 year old foodies

Colors
0355a3
eaf1f7

Requirements
Must have
• FERNHOLLOW (label name)
Estate,
Red Wine Blend NV,

```html
<!DOCTYPE html>
<html lang="en">
<head>
<meta charset="utf-8">
<title>Fernhollow Estate – Red Wine Blend NV Label</title>
<link rel="stylesheet" href="https://fonts.googleapis.com/css2?family=Cormorant+Garamond:wght@500&family=Poiret+One&display=swap">
<style>
  :root {
    --backdrop: #2f4352;
    --label-ink: #22252b;
    --brand-blue: #1b8fd2;
    --deep-blue: #0355a3;
    --ice: #eaf1f7;
    --copper: #b9773a;
    --ember: #d4502a;
    --navy: #0f2556;
    --rule-grey: #8e949c;
  }
  * { margin: 0; padding: 0; box-sizing: border-box; }
  html, body { width: 1200px; height: 1200px; overflow: hidden; }
  body {
    background: radial-gradient(circle at 50% 45%, #3b5264 0%, var(--backdrop) 55%, #263845 100%);
    position: relative;
  }
  .front-label {
    position: absolute;
    left: 260px;
    top: 61px;
    width: 680px;
    height: 1078px;
    background: var(--label-ink);
    box-shadow: 0 20px 50px rgba(0,0,0,0.35);
    overflow: hidden;
  }
  .art-band {
    position: absolute;
    left: 0;
    width: 100%;
  }
  .art-band--top {
    top: 0;
    height: 124px;
    background: linear-gradient(180deg, var(--navy) 0%, #6a5a4a 35%, var(--deep-blue) 65%, #9fb8d6 100%);
  }
  .art-band--bottom {
    top: 612px;
    height: 418px;
    background: linear-gradient(180deg, #cfdcea 0%, var(--deep-blue) 22%, var(--navy) 42%, #5c4f46 58%, var(--deep-blue) 74%, #a9c0db 86%, var(--navy) 100%);
  }
  .rule {
    position: absolute;
    left: 0;
    width: 100%;
    height: 3px;
    background: linear-gradient(90deg, var(--ember), var(--copper) 20%, var(--copper) 80%, var(--ember));
  }
  .rule--top { top: 140px; }
  .rule--bottom { top: 1046px; }
  .brand-dot {
    position: absolute;
    left: 50%;
    top: 184px;
    width: 76px;
    height: 76px;
    margin-left: -38px;
    border-radius: 50%;
    background: var(--brand-blue);
  }
  .brand-name {
    position: absolute;
    top: 318px;
    width: 100%;
    text-align: center;
    font-family: "Poiret One", sans-serif;
    font-weight: 400;
    font-size: 78px;
    line-height: 1;
    letter-spacing: 3px;
    color: var(--brand-blue);
    transform: scaleY(1.35);
  }
  .estate {
    position: absolute;
    top: 456px;
    width: 100%;
    text-align: center;
    font-family: "Cormorant Garamond", serif;
    font-weight: 500;
    font-size: 56px;
    line-height: 1;
    color: var(--ice);
  }
  .blend-line {
    position: absolute;
    left: 50%;
    width: 440px;
    margin-left: -220px;
    height: 2px;
    background: var(--rule-grey);
  }
  .blend-line--over { top: 538px; }
  .blend-line--under { top: 590px; }
  .blend {
    position: absolute;
    top: 546px;
    width: 100%;
    text-align: center;
    font-family: "Cormorant Garamond", serif;
    font-weight: 500;
    font-size: 38px;
    line-height: 1;
    letter-spacing: 1px;
    color: var(--brand-blue);
  }
</style>
</head>
<body>
  <main class="front-label">
    <div class="art-band art-band--top" role="img" aria-label="Abstract marbled artwork in blue, white and copper"></div>
    <div class="rule rule--top"></div>

    <div class="brand-dot"></div>
    <h1 class="brand-name">FERNHOLLOW</h1>
    <p class="estate">ESTATE</p>

    <div class="blend-line blend-line--over"></div>
    <p class="blend">RED WINE BLEND NV</p>
    <div class="blend-line blend-line--under"></div>

    <div class="art-band art-band--bottom" role="img" aria-label="Abstract marbled artwork in blue, white and copper"></div>
    <div class="rule rule--bottom"></div>
  </main>
</body>
</html>
```